DJ / Music Prod. studio needs Website.

Web Design needed for a DJ / Music Production Studio. Bright crisp colors, sharp, and user friendly. The design should incorporate the equalizer look that the logo has, however I am not opposed to a different idea if you feel it would look better. When someone gets to the landing page I need them to understand what our services our immediately and be able to easily navigate the content, via both text and the view trail video which will be provided and should be the centerpiece of the landing page. thx good luck!

Target Market(s)

people hosting personal parties and events.

Industry/Entity Type

Party Planning

Logo Text

SpinFreeHost.net

Number of Pages Required

4 page

Font styles to use
Sans Serif

Colors
0592cd
e24096
a54499
6b449b
00a990
000000
86cfc6

Requirements
Must have
• A page where they can submit the info directly on the site. Fill in the blanks type and coinwell button upon submission. A video box linked to our viewtrail account on the main page so the viewtrail videos to play. The 4 pages plus landing page are; 1. Pricing 2. Submit (which is also the pay page) 3 FAQ 4. Contact. Our logo can be the header, and the mirrored one could possibly be the background. I am very open minded and open to creative suggestions. you know what looks best better then I would. Please stay with the same color scheme as the main logo. I will have the full text up within a day or 2. Thx 4 reading and good luck!
Nice to have
• Each pages header the same but in a different color scheme. See zip file
Should not have
• Anything that might take away from it being sharp , clean, and user friendly. This isn't a club dj site but more of a site for everyday people of all demographics who need music for their personal parties and events.

```html
<!DOCTYPE html>
<html lang="en">
<head>
<meta charset="utf-8">
<title>SpinFreeHost.net</title>
<link rel="stylesheet" href="https://fonts.googleapis.com/css2?family=Open+Sans:wght@300;400;600;700&display=swap">
<style>
  :root {
    --black: #000000;
    --header-bg: #0b0b0d;
    --nav: #a54499;
    --nav-line: #c46abb;
    --pink: #e24096;
    --violet: #6b449b;
    --blue: #0592cd;
    --teal: #00a990;
    --section-bg: #1d1d1f;
    --band-bg: #141416;
    --footer-bg: #0b0b0d;
    --text: #ffffff;
    --muted: #b9b9bd;
  }
  * { box-sizing: border-box; margin: 0; padding: 0; }
  html, body { width: 880px; height: 1200px; overflow: hidden; background: var(--black); }
  body { font-family: "Open Sans", Arial, sans-serif; color: var(--text); position: relative; }

  .site-header { position: absolute; top: 0; left: 0; width: 880px; height: 112px; background: var(--header-bg); }
  .brand { position: absolute; left: 0; width: 880px; top: 36px; text-align: center; }
  .brand-name { display: inline-flex; align-items: center; gap: 8px; font-size: 18px; font-weight: 600; color: var(--pink); letter-spacing: 0.5px; }
  .brand-name .dot { width: 10px; height: 10px; background: var(--pink); border-radius: 50%; }
  .social { position: absolute; display: flex; gap: 6px; }
  .social span { width: 20px; height: 20px; border-radius: 50%; background: var(--text); }
  .site-header .social { right: 26px; top: 72px; }

  .main-nav { position: absolute; top: 112px; left: 0; width: 880px; height: 36px; background: var(--nav); display: flex; justify-content: center; align-items: center; }
  .main-nav a { color: var(--text); text-decoration: none; font-size: 11px; font-weight: 600; padding: 0 26px; border-left: 1px solid var(--nav-line); line-height: 14px; }
  .main-nav a:first-child { border-left: none; }

  .hero { position: absolute; top: 148px; left: 0; width: 880px; height: 437px; }
  .hero-photo { position: absolute; inset: 0; background: radial-gradient(ellipse at 50% 40%, #4a3a78 0%, #2a2350 40%, #141228 75%, #0b0a16 100%); }
  .hero-content { position: absolute; left: 0; top: 76px; width: 880px; text-align: center; }
  .hero-kicker { font-size: 26px; font-weight: 600; letter-spacing: 3px; }
  .hero-title { font-size: 76px; font-weight: 400; letter-spacing: 10px; color: var(--pink); line-height: 84px; }
  .hero-text { width: 460px; margin: 12px auto 0; font-size: 12px; line-height: 16px; color: #e6e6ea; }
  .play-button { display: block; margin: 22px auto 0; }

  .pros { position: absolute; top: 585px; left: 0; width: 880px; height: 380px; background: var(--section-bg); }
  .pros-title { position: absolute; top: 52px; width: 880px; text-align: center; font-size: 33px; font-weight: 400; }
  .pros-title em { font-style: normal; color: var(--pink); }
  .pro-card { position: absolute; top: 112px; width: 275px; }
  .pro-card.left { left: 114px; }
  .pro-card.right { left: 512px; }
  .pro-photo { height: 148px; }
  .pro-photo.decks { background: linear-gradient(135deg, #c2197e 0%, #5a2a8e 45%, #1b6fb3 100%); }
  .pro-photo.crowd { background: linear-gradient(160deg, #3a1e0e 0%, #b5651d 40%, #e8a23a 60%, #2a1a4a 100%); }
  .pro-text { margin-top: 14px; font-size: 11px; line-height: 16px; color: var(--muted); }

  .testimonials { position: absolute; top: 965px; left: 0; width: 880px; height: 163px; background: var(--band-bg); }
  .quote { position: absolute; top: 34px; width: 380px; height: 100px; }
  .quote.first { left: 56px; }
  .quote.second { left: 458px; }
  .avatar { position: absolute; left: 0; top: 0; width: 92px; height: 92px; border-radius: 50%; border: 3px solid #ffffff; }
  .avatar.one { background: linear-gradient(160deg, #d9b58a, #7a5a3e); }
  .avatar.two { background: linear-gradient(160deg, #b9a79a, #5a4e48); }
  .quote-mark { position: absolute; left: 112px; top: -6px; font-size: 46px; line-height: 46px; color: #55555c; font-family: Georgia, serif; }
  .quote-text { position: absolute; left: 144px; top: 4px; width: 216px; font-size: 10.5px; line-height: 15px; color: var(--muted); }
  .read-more { position: absolute; left: 144px; top: 66px; font-size: 11px; color: var(--pink); text-decoration: none; }

  .site-footer { position: absolute; top: 1128px; left: 0; width: 880px; height: 72px; background: var(--footer-bg); }
  .copyright { position: absolute; left: 26px; top: 30px; font-size: 10px; color: var(--muted); }
  .site-footer .social { right: 26px; top: 26px; }
</style>
</head>
<body>
  <header class="site-header">
    <div class="brand">
      <div class="brand-name"><span class="dot"></span>SpinFreeHost.net</div>
    </div>
    <div class="social" aria-label="Social links"><span></span><span></span><span></span><span></span></div>
  </header>

  <nav class="main-nav">
    <a href="#">HOME</a><a href="#">PRICING</a><a href="#">SUBMIT</a><a href="#">FAQ</a><a href="#">CONTACT</a>
  </nav>

  <section class="hero">
    <div class="hero-photo" role="img" aria-label="Photo of a DJ mixing at turntables under purple stage lights"></div>
    <div class="hero-content">
      <p class="hero-kicker">WHAT IS</p>
      <h1 class="hero-title">SFH..</h1>
      <p class="hero-text">Lorem ipsum dolor sit amet, consectetur adipiscing elit, sed do eiusmod tempor incididunt ut labore et dolore magna aliqua. Ut enim ad minim veniam, sed do eiusmod tempor.</p>
      <svg class="play-button" width="60" height="44" viewBox="0 0 60 44" aria-label="Play video">
        <circle cx="30" cy="22" r="21" fill="#e24096"/>
        <path d="M25 13 L38 22 L25 31 Z" fill="#ffffff"/>
      </svg>
    </div>
  </section>

  <section class="pros">
    <h2 class="pros-title">Pro of <em>SFH</em> over hiring a DJ</h2>
    <article class="pro-card left">
      <div class="pro-photo decks" role="img" aria-label="Photo of a DJ mixing deck in pink and blue light"></div>
      <p class="pro-text">Lorem ipsum dolor sit amet, consectetur adipiscing elit, sed do eiusmod tempor incididunt ut labore et dolore magna aliqua. Ut enim ad minim veniam.</p>
    </article>
    <article class="pro-card right">
      <div class="pro-photo crowd" role="img" aria-label="Photo of a party crowd under warm stage lights"></div>
      <p class="pro-text">Lorem ipsum dolor sit amet, consectetur adipiscing elit, sed do eiusmod tempor incididunt ut labore et dolore magna aliqua. Ut enim ad minim veniam.</p>
    </article>
  </section>

  <section class="testimonials">
    <blockquote class="quote first">
      <div class="avatar one" role="img" aria-label="Portrait of a smiling customer"></div>
      <span class="quote-mark">&ldquo;</span>
      <p class="quote-text">Lorem ipsum dolor sit amet, consectetur adipiscing elit, sed do eiusmod tempor incididunt ut labore et dolore magna aliqua. Ut enim ad.</p>
      <a class="read-more" href="#">read more</a>
    </blockquote>
    <blockquote class="quote second">
      <div class="avatar two" role="img" aria-label="Portrait of a happy customer"></div>
      <span class="quote-mark">&ldquo;</span>
      <p class="quote-text">Lorem ipsum dolor sit amet, consectetur adipiscing elit, sed do eiusmod tempor incididunt ut labore et dolore magna aliqua. Ut enim ad.</p>
      <a class="read-more" href="#">read more</a>
    </blockquote>
  </section>

  <footer class="site-footer">
    <p class="copyright">Copyright (c) 2015, SpinFreeHost.net. All Rights Reserved</p>
    <div class="social" aria-label="Social links"><span></span><span></span><span></span><span></span></div>
  </footer>
</body>
</html>
```